Looking for attractive banner design (print banner)

I am looking to redesign a banner to be more attractive and professional. This will be a print banner, 24" x 36" vertical. I am attaching the original concept to reference. High resolution file for print required. fading or blurring the background, attractive fonts, gradient highlight for text boxes, etc.

```html
<!DOCTYPE html>
<html lang="en">
<head>
<meta charset="utf-8">
<title>Essential Oils for the Horse &amp; Rider</title>
<link rel="stylesheet" href="https://fonts.googleapis.com/css2?family=Playfair+Display:wght@700;800&family=Montserrat:wght@400;700&display=swap">
<style>
  :root {
    --page: #ffffff;
    --ink: #111111;
    --body-ink: #2a2a2a;
    --sun: #efe43a;
    --meadow: #b9cf3e;
    --grass: #7f9d38;
    --shade: #4f5e28;
    --earth: #3a2818;
    --box-strong: rgba(255,255,255,0.62);
    --box-soft: rgba(255,255,255,0.34);
    --note: #ffffff;
  }
  * { box-sizing: border-box; margin: 0; padding: 0; }
  html, body { width: 834px; height: 1200px; overflow: hidden; background: var(--page); }
  .canvas { position: relative; width: 834px; height: 1200px; background: var(--page); }
  .banner { position: absolute; left: 107px; top: 143px; width: 624px; height: 931px; overflow: hidden; }
  .banner-photo {
    position: absolute; inset: 0;
    background:
      radial-gradient(ellipse 60% 30% at 50% 5%, rgba(255,248,120,0.9), rgba(255,248,120,0) 70%),
      linear-gradient(180deg, var(--sun) 0%, var(--meadow) 22%, var(--grass) 50%, var(--shade) 75%, var(--earth) 100%);
  }
  .title-block { position: absolute; top: 24px; left: 0; width: 100%; text-align: center; }
  .title {
    font-family: "Playfair Display", serif; font-weight: 800; font-size: 56px;
    line-height: 1; color: var(--ink); letter-spacing: -0.5px;
  }
  .subtitle {
    margin-top: 8px; font-family: "Montserrat", sans-serif; font-weight: 400;
    font-size: 21px; letter-spacing: 0.5px; color: var(--ink);
  }
  .oil-box {
    position: absolute; width: 181px; height: 76px; padding: 5px 10px;
    background: linear-gradient(90deg, var(--box-strong), var(--box-soft));
  }
  .oil-box.left { left: 14px; }
  .oil-box.right { left: 429px; text-align: right;
    background: linear-gradient(270deg, var(--box-strong), var(--box-soft)); }
  .oil-box h2 {
    font-family: "Playfair Display", serif; font-weight: 700; font-size: 17px;
    line-height: 20px; color: var(--ink); white-space: nowrap; letter-spacing: -0.2px;
  }
  .oil-box h2.long { font-size: 15.5px; letter-spacing: -0.4px; }
  .oil-box p {
    margin-top: 1px; font-family: "Montserrat", sans-serif; font-weight: 400;
    font-size: 10px; line-height: 12px; color: var(--body-ink);
  }
  .disclaimer {
    position: absolute; bottom: 20px; left: 0; width: 100%; text-align: center;
    font-family: "Montserrat", sans-serif; font-weight: 700; font-size: 12px;
    color: var(--note); letter-spacing: 0.3px;
  }
</style>
</head>
<body>
<div class="canvas">
  <section class="banner">
    <div class="banner-photo" role="img" aria-label="Photo of a young woman in a straw hat and plaid shirt holding the lead of a dark horse on a sunlit forest path, softly blurred"></div>

    <header class="title-block">
      <h1 class="title">Essential Oils</h1>
      <div class="subtitle">FOR THE HORSE &amp; RIDER</div>
    </header>

    <div class="oil-box left" style="top:143px"><h2>Brain</h2><p>Frankincense,<br>Mind Spark, Clear Path,<br>Cedarwood.</p></div>
    <div class="oil-box left" style="top:234px"><h2>Skin &amp; Hair</h2><p>Cedar wood, Lavender,<br>Geranium, Frankincense,<br>Myrhh.</p></div>
    <div class="oil-box left" style="top:325px"><h2>Ears</h2><p>Helychrisum,<br>Fresh Field, Tea Tree,<br>Juniper.</p></div>
    <div class="oil-box left" style="top:417px"><h2>Lungs</h2><p>B.R. , Kestrel, Eucalyptus<br>(all), Guardian, Tea Tree,<br>Azure Gold.</p></div>
    <div class="oil-box left" style="top:508px"><h2>Muscles</h2><p>Stretch Blend, Deep Soothe,<br>Marjoram, Cypress,<br>Peppermint, Highland Fir</p></div>
    <div class="oil-box left" style="top:599px"><h2>Immune Support</h2><p>Guardian, Oregano, Ocatea,<br>Evergreen, Lemon,<br>Peppermint, Cinnamon-Bark,<br>Rosemary.</p></div>
    <div class="oil-box left" style="top:690px"><h2 class="long">Tendons &amp; Ligaments</h2><p>Palo Santo, Lemongrass, . .<br>Rosemary, peppermint.</p></div>
    <div class="oil-box left" style="top:781px"><h2>Hoof (Horse)</h2><p>Guardian, Tea Tree,<br>Oregano, Frankincense.</p></div>

    <div class="oil-box right" style="top:143px"><h2>Emotional Support</h2><p>Courage, Solace, Full Stride,<br>Bright Heart, Lemon.</p></div>
    <div class="oil-box right" style="top:234px"><h2>Eyes</h2><p>Frankincense,<br>Sandalwood,<br>Carrot Seed, Lemongrass.</p></div>
    <div class="oil-box right" style="top:325px"><h2>Mouth</h2><p>Clove, Ocatea, Tea Tree,<br>Wintergreen, Guardian.</p></div>
    <div class="oil-box right" style="top:417px"><h2>Heart</h2><p>Orange, Ylang Ylang,<br>Cypress, Helichrysum,<br>Palmarosa.</p></div>
    <div class="oil-box right" style="top:508px"><h2>Digestion</h2><p>Gut Calm, Easy Ride,<br>Ginger, Fennel,<br>Peppermint.</p></div>
    <div class="oil-box right" style="top:599px"><h2>Hormonal Balance</h2><p>Clary Sage, Moon Cycle,<br>Balance Flow, Myrtle,<br>Azure Gold.</p></div>
    <div class="oil-box right" style="top:690px"><h2>Bones &amp; Joints</h2><p>Ache Relief, Helichrysum,<br>Wintergreen, Cool Blue,<br>Courage.</p></div>
    <div class="oil-box right" style="top:781px"><h2>Feets (Rider)</h2><p>Steady Earth, Courage,<br>Guardian, Fresh Field,<br>Oregano.</p></div>

    <p class="disclaimer">_- DISCLAIMER: NOT EVALUATED BY THE FDA, NOT MEDICAL ADVICE. -</p>
  </section>
</div>
</body>
</html>
```